Equipment Finance Specialist I work with companies who need the funds to buy their equipment

I would like a business card that stands out on the shelves. I want to be able to hand it to someone and say WOW. This card should have my logo.
You can put color into it I am very open on design and color

What my company does is we deal with dealerships that sell equipment such as Dump Trucks garbage trucks tractors trailers. Customers get referred to us and depending on their time in business we will ask for the following items

Companies that have been in business for more than two years we have a credit application program up to 250K . With this program we need the following items Credit application filled out(which is what I would like to be able for the customer to click on my website to get.) as well as three current month bank statements.

Deals over 250k we will need the following items

2 years business tax returns
2 years personal tax returns
Profit & Loss statement
Personal Financial Statement

what we do
100% FINANCING
SEASONAL PAYMENTS
LOAN BALLOON PAYMENTS
TRAC LEASING
LOW-INTEREST REFINANCING RATES
DEBT CONSOLIDATION

We specialize in creative financing solutions and offer a variety of reliable, flexible and expandable lending choices.

Target Market(s)

Trucking Companies

Industry/Entity Type

Trucking Company

Contact Information for Business Card

* $250,000 Application only Program
* Loans from $30,000 to 5,000,000
* Competitive Interest Rates

Font styles to use
Serif
Sans Serif

Colors

Designer to choose colors to be used in the design.

Requirements
Must have
• On the back of the card.
• * $250,000 Application only Program
• * Loans from $30,000 to 5,000,000
• My name, email, website. address
• * Competitive Interest Rates
• * 100% Financing
Nice to have
• I want my logo to pop on the card
• My logo is the great one I would like to use
Should not have
• I am up for your creativity as well

```html
<!DOCTYPE html>
<html lang="en">
<head>
<meta charset="utf-8">
<title>Quarvel Lending – Business Card</title>
<link href="https://fonts.googleapis.com/css2?family=Open+Sans:wght@400;600;700;800&family=Tinos:wght@700&display=swap" rel="stylesheet">
<style>
  :root{
    --bg:#e9ebef;
    --navy:#1f3475;
    --red:#d9232e;
    --white:#ffffff;
    --ink:#1a1a1a;
    --black:#141414;
    --black-soft:#2a2a2a;
    --silver:#d6d8dc;
  }
  *{margin:0;padding:0;box-sizing:border-box}
  html,body{width:1200px;height:900px;overflow:hidden;background:var(--bg)}
  body{font-family:"Open Sans",Arial,sans-serif;position:relative}

  .card{position:absolute;left:320px;width:560px;height:320px;border-radius:22px;overflow:hidden;box-shadow:0 10px 28px rgba(0,0,0,.18)}
  .card--front{top:70px;background:var(--white)}
  .card--back{top:470px;background:radial-gradient(ellipse at 40% 35%,var(--black-soft),var(--black) 75%)}

  .front-shape{position:absolute;inset:0}

  .brand{position:absolute;display:flex;align-items:center;gap:10px;white-space:nowrap}
  .brand__dot{border-radius:50%;flex:none}
  .brand__name{font-weight:800;letter-spacing:.5px;text-transform:uppercase;line-height:1;white-space:nowrap}

  .card--front .brand{left:26px;top:26px}
  .card--front .brand__dot{width:40px;height:40px;background:var(--navy)}
  .card--front .brand__name{font-size:24px;color:var(--navy)}

  .card--back .brand{left:50%;top:50%;transform:translate(-50%,-50%);gap:16px}
  .card--back .brand__dot{width:64px;height:64px;border:5px solid var(--silver)}
  .card--back .brand__name{font-size:36px;color:var(--silver)}

  .perks{position:absolute;left:24px;top:176px;list-style:none;color:var(--white);font-size:13px;line-height:1.55}
  .perks li::before{content:"• ";}

  .contact{position:absolute;left:300px;top:84px;color:var(--ink)}
  .contact__name{font-family:"Tinos","Times New Roman",serif;font-weight:700;font-size:21px;letter-spacing:.3px}
  .contact__role{color:var(--navy);font-size:15px;margin-top:2px;padding-bottom:4px;border-bottom:2px solid var(--navy);width:66px}
  .contact__list{list-style:none;margin-top:10px;font-size:15px;line-height:1.5}
  .contact__list li{display:flex;align-items:center;gap:8px;white-space:nowrap}
  .contact__list svg{width:13px;height:13px;flex:none}

  .address{position:absolute;right:34px;bottom:26px;color:var(--white);font-size:17px;display:flex;align-items:center;gap:8px}
  .address svg{width:12px;height:16px}
</style>
</head>
<body>

<section class="card card--front">
  <svg class="front-shape" viewBox="0 0 560 320" preserveAspectRatio="none" aria-hidden="true">
    <path d="M0 152 H236 Q262 152 266 180 L270 214 Q274 240 300 240 H560 V320 H0 Z" fill="var(--navy)"/>
    <path d="M266 190 L270 214 Q274 240 300 240 H560 V228 H302 Q284 228 281 210 L278 190 Z" fill="var(--red)"/>
  </svg>

  <div class="brand">
    <span class="brand__dot"></span>
    <span class="brand__name">Quarvel Lending</span>
  </div>

  <ul class="perks">
    <li>$250,000 Application only Program</li>
    <li>Loans from $30,000 to 5,000,000</li>
    <li>Competitive Interest Rates</li>
    <li>100% Financing</li>
  </ul>

  <div class="contact">
    <p class="contact__name">YOUR NAME</p>
    <p class="contact__role">Position</p>
    <ul class="contact__list">
      <li><svg viewBox="0 0 24 24"><path fill="var(--navy)" d="M6.6 10.8a15 15 0 0 0 6.6 6.6l2.2-2.2a1 1 0 0 1 1-.25 11.4 11.4 0 0 0 3.6.57 1 1 0 0 1 1 1V20a1 1 0 0 1-1 1A17 17 0 0 1 3 4a1 1 0 0 1 1-1h3.5a1 1 0 0 1 1 1c0 1.25.2 2.450 .57 3.6a1 1 0 0 1-.25 1z"/></svg>phone number</li>
      <li><svg viewBox="0 0 24 24"><rect x="2" y="5" width="20" height="14" fill="none" stroke="var(--navy)" stroke-width="2"/><path d="M2 5l10 8 10-8" fill="none" stroke="var(--navy)" stroke-width="2"/></svg>info@quarvellending.com</li>
      <li><svg viewBox="0 0 24 24"><circle cx="12" cy="12" r="10" fill="none" stroke="var(--navy)" stroke-width="2"/><path d="M2 12h20M12 2c3 3 3 17 0 20M12 2c-3 3-3 17 0 20" fill="none" stroke="var(--navy)" stroke-width="1.6"/></svg>quarvellending.com</li>
    </ul>
  </div>

  <p class="address"><svg viewBox="0 0 12 16"><path fill="var(--white)" d="M6 0a6 6 0 0 0-6 6c0 4.5 6 10 6 10s6-5.5 6-10a6 6 0 0 0-6-6zm0 8.5A2.5 2.5 0 1 1 6 3.5a2.5 2.5 0 0 1 0 5z"/></svg>office address</p>
</section>

<section class="card card--back">
  <div class="brand">
    <span class="brand__dot"></span>
    <span class="brand__name">Quarvel Lending</span>
  </div>
</section>

</body>
</html>
```